Letterhead and Stationary for Construction Company

Brisk Current needs modern Letterhead, Envelopes and Notepad designs.

Industry/Entity Type

Construction

Colors
f78f20
34a7d8
ffffff

Requirements
Must have
• Modern looking design.

```html
<!DOCTYPE html>
<html lang="en">
<head>
<meta charset="utf-8">
<title>Brisk Current — Stationery</title>
<link rel="stylesheet" href="https://fonts.googleapis.com/css2?family=Montserrat:wght@500;700&display=swap">
<style>
  :root {
    --backdrop: #d2d2d2;
    --paper: #f1f1f1;
    --brand-blue: #0e6db3;
    --brand-orange: #f26f1c;
    --ink: #555;
  }
  * { margin: 0; padding: 0; box-sizing: border-box; }
  html, body { width: 1200px; height: 1041px; overflow: hidden; }
  body { background: var(--backdrop); position: relative; font-family: "Montserrat", sans-serif; }

  .sheet { position: absolute; background: var(--paper); box-shadow: 0 1px 3px rgba(0,0,0,.18); overflow: hidden; }
  .wave { position: absolute; left: 0; bottom: 0; width: 100%; height: 7px; display: block; }
  .wave path { fill: var(--brand-blue); }

  .wordmark { position: absolute; color: var(--brand-blue); font-weight: 700; white-space: nowrap; letter-spacing: -0.01em; line-height: 1; }
  .wordmark .dot { display: inline-block; width: .8em; height: .8em; border-radius: 50%; background: var(--brand-orange); margin-right: .3em; vertical-align: -0.08em; }

  .contact { position: absolute; font-size: 5.2px; color: var(--ink); line-height: 1.3; font-weight: 500; }
  .contact li { list-style: none; display: flex; align-items: center; gap: 3px; }
  .contact .icon { width: 4px; height: 4px; border-radius: 1px; background: var(--brand-blue); flex: none; }
  .address { margin-top: 4px; }

  /* folder */
  .folder { left: 166px; top: 76px; width: 416px; height: 541px; }
  .folder .spine { position: absolute; left: 24px; top: 0; bottom: 0; width: 1px; background: #dcdcdc; box-shadow: 2px 0 2px rgba(0,0,0,.05); }
  .folder .wordmark { left: 50%; transform: translateX(-50%); top: 460px; font-size: 29px; }
  .folder .web { position: absolute; left: 0; right: 0; top: 498px; text-align: center; font-size: 7.5px; color: var(--brand-blue); font-weight: 500; }

  /* letterhead */
  .letterhead { left: 615px; top: 95px; width: 403px; height: 522px; }
  .letterhead .wordmark { left: 30px; top: 31px; font-size: 17px; }
  .letterhead .contact { left: 302px; top: 26px; }

  /* envelope front */
  .envelope-front { left: 132px; top: 645px; width: 451px; height: 195px; }
  .envelope-front .wordmark { left: 20px; top: 23px; font-size: 17px; }
  .envelope-front .address { position: absolute; left: 20px; top: 162px; font-size: 5.2px; color: var(--ink); line-height: 1.35; font-weight: 500; }

  /* envelope back */
  .envelope-back { left: 615px; top: 645px; width: 451px; height: 195px; }
  .envelope-back .flap { position: absolute; left: 0; top: 0; width: 451px; height: 64px; display: block; }
  .envelope-back .flap path { fill: var(--brand-blue); }
  .envelope-back .seal { position: absolute; left: 213px; top: 20px; width: 24px; height: 24px; border-radius: 50%; background: var(--brand-orange); }

  /* business cards */
  .card-front { left: 417px; top: 870px; width: 167px; height: 96px; }
  .card-front .person { position: absolute; left: 13px; top: 21px; }
  .card-front .name { font-size: 5.2px; font-weight: 700; color: var(--brand-blue); text-transform: uppercase; }
  .card-front .role { font-size: 3.6px; color: var(--ink); margin-top: 1px; }
  .card-front .wordmark { right: 12px; top: 20px; font-size: 10px; }
  .card-front .contact { left: 13px; top: 62px; font-size: 3.7px; }
  .card-front .contact .icon { width: 3px; height: 3px; }
  .card-front .card-address { position: absolute; right: 13px; top: 74px; font-size: 3.7px; color: var(--ink); text-align: right; line-height: 1.35; }

  .card-back { left: 615px; top: 870px; width: 167px; height: 96px; background: var(--brand-blue); }
  .card-back .wordmark { left: 50%; transform: translateX(-50%); top: 38px; font-size: 14px; color: #fff; }
  .card-back .web { position: absolute; left: 0; right: 0; top: 62px; text-align: center; font-size: 3.8px; color: #fff; }
</style>
</head>
<body>

<section class="sheet folder" aria-label="Presentation folder">
  <div class="spine"></div>
  <p class="wordmark">Brisk Current</p>
  <p class="web">www.briskcurrent.com</p>
  <svg class="wave" viewBox="0 0 100 7" preserveAspectRatio="none"><path d="M0 7 Q50 -1 100 7 Z"/></svg>
</section>

<section class="sheet letterhead" aria-label="Letterhead">
  <p class="wordmark"><span class="dot"></span>Brisk Current</p>
  <ul class="contact">
    <li><span class="icon"></span>305-555-0142</li>
    <li><span class="icon"></span>877-555-0198</li>
    <li><span class="icon"></span>info@briskcurrent.com</li>
    <li><span class="icon"></span>www.briskcurrent.com</li>
    <li class="address">2260 Harbor Point Rd.<br>Suite 410, Bayview</li>
  </ul>
  <svg class="wave" viewBox="0 0 100 7" preserveAspectRatio="none"><path d="M0 7 Q50 -1 100 7 Z"/></svg>
</section>

<section class="sheet envelope-front" aria-label="Envelope front">
  <p class="wordmark"><span class="dot"></span>Brisk Current</p>
  <p class="address">2260 Harbor Point Rd.<br>Suite 410, Bayview</p>
  <svg class="wave" viewBox="0 0 100 7" preserveAspectRatio="none"><path d="M0 7 Q50 -1 100 7 Z"/></svg>
</section>

<section class="sheet envelope-back" aria-label="Envelope back">
  <svg class="flap" viewBox="0 0 451 64"><path d="M0 0 H451 L435 61 Q434 64 430 64 H21 Q17 64 16 61 Z"/></svg>
  <span class="seal"></span>
</section>

<section class="sheet card-front" aria-label="Business card front">
  <div class="person">
    <p class="name">Jordan Mercer</p>
    <p class="role">Director</p>
  </div>
  <p class="wordmark"><span class="dot"></span>Brisk Current</p>
  <ul class="contact">
    <li><span class="icon"></span>305-555-0142</li>
    <li><span class="icon"></span>877-555-0198</li>
    <li><span class="icon"></span>info@briskcurrent.com</li>
    <li><span class="icon"></span>www.briskcurrent.com</li>
  </ul>
  <p class="card-address">2260 Harbor Point Rd.<br>Suite 410, Bayview</p>
  <svg class="wave" viewBox="0 0 100 7" preserveAspectRatio="none" style="height:4px"><path d="M0 7 Q50 -1 100 7 Z"/></svg>
</section>

<section class="sheet card-back" aria-label="Business card back">
  <p class="wordmark">Brisk Current</p>
  <p class="web">www.briskcurrent.com</p>
</section>

</body>
</html>
```